Marcus Feldwick Carpentry & Joinery

Hello, I would like a flyer designed for my new business doing small projects in my local area for home-owners. I am a professional tradesman.
The type of work I am offering is:
- decks/decking
- external stairs & railings
- install windows & doors
- roofs & gutters
- small additions
- built-in wardrobes
- finish work
- demolition

It would be great if the flyer could mention these, or use phrasing that fits this kind of construction work.
My idea for a slogan was "new work and repairs to any age home".

Please also mention FREE QUOTES and have my email and phone number included on the flyer, along with my carpentry licence number, which I can provided.

I'd like a one page, single-sided flyer that could be printed as DL.
Colour and style is up to you! I'll be placing this flyer on counters & in the windows of local businesses, so something simple and eye-catching is preferred.

Thank you!

```html
<!DOCTYPE html>
<html lang="en">
<head>
<meta charset="utf-8">
<title>Carpentry &amp; Joinery Flyer</title>
<link rel="stylesheet" href="https://fonts.googleapis.com/css2?family=Exo+2:wght@700;800&family=Archivo:wght@800&family=Roboto:wght@400;700&display=swap">
<style>
  :root {
    --orange: #f37a1f;
    --amber: #f39c12;
    --grey: #808285;
    --text-grey: #6d6e71;
    --white: #ffffff;
    --ink: #111111;
  }
  html, body { margin: 0; padding: 0; overflow: hidden; background: var(--white); }
  .flyer {
    position: relative;
    width: 1200px;
    height: 2178px;
    overflow: hidden;
    background: var(--white);
    font-family: "Roboto", Arial, sans-serif;
  }
  .bands { position: absolute; inset: 0; }
  .logo-badge {
    position: absolute;
    left: 60px; top: 50px;
    width: 250px; height: 250px;
    border-radius: 50%;
    background: var(--white);
    display: flex; align-items: center; justify-content: center;
    font-weight: 700;
    font-size: 52px;
    color: var(--ink);
  }
  .slogan {
    position: absolute;
    left: 421px; top: 78px;
    margin: 0;
    font-family: "Exo 2", Arial, sans-serif;
    font-weight: 800;
    font-size: 64px;
    line-height: 72px;
    color: var(--white);
    white-space: nowrap;
  }
  .services-title {
    position: absolute;
    left: 104px; top: 515px;
    margin: 0;
    font-family: "Exo 2", Arial, sans-serif;
    font-weight: 800;
    font-size: 88px;
    line-height: 100px;
    color: var(--orange);
    white-space: nowrap;
  }
  .services-list {
    position: absolute;
    left: 107px; top: 628px;
    margin: 0; padding: 0;
    list-style: none;
  }
  .services-list li {
    position: relative;
    padding-left: 69px;
    height: 85px;
    font-family: "Archivo", Arial, sans-serif;
    font-weight: 800;
    font-size: 62px;
    line-height: 85px;
    color: var(--text-grey);
    white-space: nowrap;
  }
  .services-list li::before {
    content: "";
    position: absolute;
    left: 0; top: 25px;
    width: 22px; height: 22px;
    border: 7px solid var(--orange);
    border-radius: 50%;
  }
  .photo { position: absolute; }
  .photo-tradesman {
    left: 795px; top: 905px;
    width: 380px; height: 865px;
    border-radius: 170px 170px 30px 30px;
    background: linear-gradient(180deg, #f2c318 0%, #e0b08e 18%, #3f6fb2 40%, #355f9c 70%, #9a6a3a 92%);
  }
  .photo-assistant {
    left: 48px; top: 1588px;
    width: 350px; height: 590px;
    border-radius: 170px 170px 0 0;
    background: linear-gradient(180deg, #5a3a28 0%, #d9a98a 30%, #f4f4f4 55%, #e9e9e9 100%);
  }
  .quote-button {
    position: absolute;
    left: 191px; top: 1399px;
    width: 640px; height: 119px;
    background: var(--orange);
    border-radius: 26px 0 0 26px;
  }
  .quote-label {
    position: absolute;
    left: 228px; top: 1399px;
    height: 119px;
    margin: 0;
    display: flex; align-items: center;
    font-family: "Exo 2", Arial, sans-serif;
    font-weight: 800;
    font-size: 64px;
    color: var(--white);
    white-space: nowrap;
  }
  .call-line {
    position: absolute;
    left: 421px; top: 1868px;
    margin: 0;
    font-weight: 700;
    font-size: 46px;
    line-height: 70px;
    color: var(--white);
    white-space: nowrap;
  }
  .call-line .phone { font-size: 62px; margin-left: 10px; }
  .contact-details {
    position: absolute;
    left: 617px; top: 1968px;
    list-style: none;
    margin: 0; padding: 0;
    font-size: 33px;
    line-height: 45px;
    color: var(--white);
  }
  .contact-details li { display: flex; align-items: center; gap: 14px; white-space: nowrap; }
  .contact-details svg { width: 26px; height: 26px; flex: none; }
  .licence {
    position: absolute;
    left: 606px; top: 2108px;
    margin: 0;
    font-weight: 700;
    font-size: 43px;
    line-height: 50px;
    color: var(--white);
    white-space: nowrap;
  }
</style>
</head>
<body>
<div class="flyer">
  <svg class="bands" viewBox="0 0 1200 2178" width="1200" height="2178" aria-hidden="true">
    <defs>
      <linearGradient id="headerFill" x1="0" y1="0" x2="1" y2="0">
        <stop offset="0" stop-color="#f37a1f"/>
        <stop offset="1" stop-color="#f39c12"/>
      </linearGradient>
      <linearGradient id="footerFill" x1="0" y1="0" x2="1" y2="0">
        <stop offset="0" stop-color="#f39c12"/>
        <stop offset="1" stop-color="#f37a1f"/>
      </linearGradient>
    </defs>
    <path d="M0,0 H1200 V472 C900,300 380,300 0,500 Z" fill="var(--grey)"/>
    <path d="M0,0 H1200 V420 C900,280 380,280 0,445 Z" fill="url(#headerFill)"/>
    <path d="M0,1900 C320,1700 800,1690 1200,1760 V2178 H0 Z" fill="var(--grey)"/>
    <path d="M0,1950 C320,1750 800,1745 1200,1815 V2178 H0 Z" fill="url(#footerFill)"/>
  </svg>

  <div class="logo-badge">Logo</div>
  <h1 class="slogan">New work and repairs<br>to any age home</h1>

  <h2 class="services-title">Offering Services:</h2>
  <ul class="services-list">
    <li>Decks/Decking</li>
    <li>External Stairs &amp; Railings</li>
    <li>Install Windows &amp; Doors</li>
    <li>Roofs &amp; Gutters</li>
    <li>Small Additions</li>
    <li>Built-in Wardrobes</li>
    <li>Finish Work</li>
    <li>Demolition</li>
  </ul>

  <div class="quote-button"></div>
  <p class="quote-label">FREE QUOTES</p>
  <div class="photo photo-tradesman" role="img" aria-label="Photo of a smiling tradesman in a yellow hard hat, blue shirt and tool belt, arms crossed"></div>

  <div class="photo photo-assistant" role="img" aria-label="Photo of a smiling customer service assistant with a headset, in a white blazer"></div>

  <p class="call-line">Call Us :<span class="phone">888-888-8888</span></p>
  <ul class="contact-details">
    <li>
      <svg viewBox="0 0 24 24"><path d="M12 1a8 8 0 0 0-8 8c0 6 8 14 8 14s8-8 8-14a8 8 0 0 0-8-8zm0 11a3 3 0 1 1 0-6 3 3 0 0 1 0 6z" fill="#fff"/></svg>
      Street Address City Pin code
    </li>
    <li>
      <svg viewBox="0 0 24 24"><circle cx="12" cy="12" r="10" fill="none" stroke="#fff" stroke-width="2.5"/><path d="M2 12h20M12 2c3 3 3 17 0 20M12 2c-3 3-3 17 0 20" fill="none" stroke="#fff" stroke-width="2"/></svg>
      support@companyname.com
    </li>
    <li>
      <svg viewBox="0 0 24 24"><rect x="2" y="5" width="20" height="14" fill="none" stroke="#fff" stroke-width="2.5"/><path d="M2 5l10 8 10-8" fill="none" stroke="#fff" stroke-width="2.5"/></svg>
      www.companyname.com
    </li>
  </ul>
  <p class="licence">licence no. 888888</p>
</div>
</body>
</html>
```